COMMERCIAL REAL ESTATE FLYER TEMPLATE

We need a template flyer designed that we can use for a current commercial real estate listing and subsequently use as a template for future listings. We have uploaded images and files to provide an example of an older flyer template we have used. If you have questions or would like to discuss, please contact us at Wade@TLMVX.net. Colors selected should be in line with our attached business card and logo design. Output should be 8.5" X 11".

Target Market(s)

Commercial Real Estate. NO RESIDENTIAL. Needs to have a professional commercial presentation with no reference to residential real estate.

Industry/Entity Type

Real Estate Agent

Font styles to use
Serif

Colors

Designer to choose colors to be used in the design.

Requirements
Must have
• MUST BE SAVED AND ADJUSTABLE IN ONE OF THE FOLLOWING FORMATES: MICROSOFT POWERPOINT, PUBLISHER OR WORD. THIS IS IMPORTANT SO OUR TEAM CAN EASILLY UPDATE TEMPLATE IN READILLY AVAILABLE PROGRAMS THAT ARE SIMPLE FOR TEAM MEMBERS TO USE.
Nice to have
• Needs to have first page template with header and footer displaying our logo, address, phone, email address and contact information for the listing agent. There need to be placeholders that can be easily adjusted based on specific listings. Placeholders will be used for pictures or aerials as the case requires. Needs to have a second page that has header and footer with a clean open block in the middle of the page so agents can customize with site specific details.
Should not have
• There should be no reference to residential. We are a commercial real estate organization that does not do any residential.

```html
<!DOCTYPE html>
<html lang="en">
<head>
<meta charset="utf-8">
<title>Flex Industrial Listing Flyer</title>
<link href="https://fonts.googleapis.com/css2?family=Anton&family=Arimo:wght@400;700&display=swap" rel="stylesheet">
<style>
  :root {
    --backdrop: #8a8a8a;
    --paper: #ffffff;
    --brand-red: #c0202a;
    --frame-red: #c41e2a;
    --footer-gray: #434343;
    --ink: #1e1e1e;
    --white: #ffffff;
  }
  * { box-sizing: border-box; margin: 0; padding: 0; }
  html, body { width: 1200px; height: 1200px; overflow: hidden; }
  body { background: var(--backdrop); position: relative; font-family: "Arimo", Arial, sans-serif; color: var(--ink); }

  .page { position: absolute; top: 287px; width: 492px; height: 633px; background: var(--paper); overflow: hidden; box-shadow: 0 3px 8px rgba(0,0,0,.25); }
  .page--front { left: 81px; }
  .page--details { left: 624px; }

  .abs { position: absolute; }
  .photo { position: absolute; }
  .photo--office { background: linear-gradient(160deg, #a7a07a 0%, #8d8460 45%, #b9a98a 75%, #6e6654 100%); }
  .photo--desk { background: linear-gradient(170deg, #8a7f5e 0%, #a0825a 50%, #7a4f38 80%, #b84a3c 100%); }
  .photo--exterior { background: linear-gradient(180deg, #8fb4d8 0%, #c9dbec 40%, #a9876d 62%, #8a6a55 80%, #8d8a80 100%); }
  .photo--study { background: linear-gradient(160deg, #6e4a2e 0%, #9a8a62 40%, #b9ac8a 70%, #7b5338 100%); }
  .photo--kitchen { background: linear-gradient(170deg, #9ea579 0%, #b07a3e 45%, #c8b79a 80%, #a89a80 100%); }
  .photo--warehouse { background: linear-gradient(180deg, #4a4a52 0%, #9aa0a8 40%, #6a6a6a 55%, #b6b8ba 75%, #9ea1a3 100%); }
  .map { background: linear-gradient(135deg, #e9ebe4 0%, #dfe4dc 50%, #eceee8 100%); }

  .brand-mark { position: absolute; background: var(--brand-red); color: var(--white); display: flex; flex-direction: column; align-items: center; justify-content: center; text-align: center; font-weight: 700; font-size: 11px; line-height: 1.25; letter-spacing: .3px; }

  .title-block { position: absolute; background: var(--brand-red); color: var(--white); padding: 14px 0 0 14px; }
  .title-block h1 { font-family: "Anton", Impact, sans-serif; font-weight: 400; font-size: 28px; line-height: 33.6px; letter-spacing: .4px; }
  .title-block p { font-size: 13.5px; line-height: 17px; margin-top: 10px; }

  .framed { position: absolute; border: 1.5px solid var(--frame-red); }
  .framed--thick { border-width: 3px; }

  .facts { position: absolute; left: 252px; top: 302px; font-size: 9.3px; line-height: 14px; }
  .facts h2 { font-weight: 400; font-size: 11px; line-height: 13px; margin-bottom: 1px; }
  .disclaimer { position: absolute; left: 250px; top: 472px; width: 229px; font-size: 7.6px; line-height: 10.3px; text-align: justify; }

  .footer { position: absolute; left: 0; width: 100%; background: var(--footer-gray); color: var(--white); }
  .footer--front { top: 612px; height: 21px; font-size: 9px; }
  .footer--details { top: 538px; height: 95px; font-size: 14px; }
  .contact { position: absolute; display: flex; align-items: center; gap: 8px; }
  .contact svg { flex: none; }

  .config { position: absolute; font-size: 7.2px; line-height: 14px; }
  .config h3 { color: var(--brand-red); font-size: 8px; font-weight: 700; line-height: 14px; }
  .config ul { list-style: none; }
  .config li::before { content: "\2022\00a0"; }
</style>
</head>
<body>

<section class="page page--front">
  <div class="photo photo--office" style="left:0;top:0;width:492px;height:272px" role="img" aria-label="Interior photo of an office workstation with monitor and stool"></div>
  <div class="brand-mark" style="left:22px;top:15px;width:96px;height:78px"><span>WADE HARLOW</span><span>COMMERCIAL REAL ESTATE</span></div>
  <div class="title-block" style="left:246px;top:90px;width:240px;height:201px">
    <h1>FLEX INDUSTRIAL<br>FOR SALE OR<br>LEASE - HOUSTON,<br>TEXAS</h1>
    <p>4810 Ridgeway Commerce Dr., Houston, Texas 77073</p>
  </div>

  <div class="framed" style="left:8px;top:297px;width:477px;height:164px"></div>
  <div class="photo photo--desk" style="left:10px;top:299px;width:231px;height:160px" role="img" aria-label="Photo of an executive office with desk, armchairs and rug"></div>
  <div class="facts">
    <h2>FLEX INDUSTRIAL - FOR SALE OR LEASE</h2>
    Well Maintained Owner - Occupied Building<br>
    Great Location Near IAH &amp; The Woodlands<br>
    Easy Access to Hardy , IH-45 &amp; Beltway 8<br>
    Building Area : 11,820 SF (HCAD)<br>
    Land Area : 41,616 SF (HCAD)<br>
    Office Build - Out : Approx. 2,820 SF (Owner)<br>
    Loading : Three (3) Grade-Level<br>
    Eave Height : Approx. 22'<br>
    Outside Storage : Room To Add Fenced Yard<br>
    ECONOMIC TERMS : Contact Broker
  </div>

  <div class="framed" style="left:8px;top:467px;width:477px;height:142px"></div>
  <div class="photo photo--exterior" style="left:10px;top:469px;width:231px;height:138px" role="img" aria-label="Exterior photo of the brick warehouse with loading doors"></div>
  <p class="disclaimer">The information contained herein has, we believe, been obtained from reliable sources,and we have no reason to doubt the accuracy thereof. All such information is submitted,subject to errors, omissions or changes in condition prior to sale, lease or withdrawal without notice. All information contained herein should be verified by the person relying thereon. We have not made and will not make any warranty or representation as to the condition of the property nor the presence of any hazardous substances or any environmental or other conditions that may asect the value or suitability of the property.</p>

  <div class="footer footer--front">
    <div class="contact" style="left:53px;top:5px">
      <svg width="11" height="11" viewBox="0 0 20 20"><circle cx="10" cy="10" r="8.5" fill="none" stroke="#fff" stroke-width="1.6"/><path d="M7 5.5l1.6 2.2-1 1.2c.6 1.3 1.6 2.3 2.9 2.9l1.2-1 2.2 1.6-.9 1.6c-3.6-.4-6.3-3.1-6.7-6.7z" fill="#fff"/></svg>
      <span>(555)014-2287</span>
    </div>
    <div class="contact" style="left:283px;top:5px">
      <svg width="11" height="9" viewBox="0 0 20 14"><rect x="1" y="1" width="18" height="12" fill="none" stroke="#fff" stroke-width="1.6"/><path d="M1 1l9 7 9-7" fill="none" stroke="#fff" stroke-width="1.6"/></svg>
      <span>Wade@TLMVX.net</span>
    </div>
  </div>
</section>

<section class="page page--details">
  <div class="photo photo--study" style="left:0;top:0;width:492px;height:250px" role="img" aria-label="Interior photo of a private office with bookcase, desk and leather sofa"></div>
  <div class="brand-mark" style="left:382px;top:15px;width:96px;height:78px"><span>WADE HARLOW</span><span>COMMERCIAL REAL ESTATE</span></div>
  <div class="title-block" style="left:11px;top:72px;width:238px;height:200px">
    <h1>FLEX INDUSTRIAL<br>FOR SALE OR<br>LEASE - HOUSTON,<br>TEXAS</h1>
    <p>4810 Ridgeway Commerce Dr., Houston, Texas 77073</p>
  </div>

  <div class="framed" style="left:8px;top:282px;width:266px;height:196px"></div>
  <div class="config" style="left:15px;top:284px">
    <h3>Office Configuration :</h3>
    <ul>
      <li>(1) 14' X 16' Executive Office</li>
      <li>(2) 14' X 12' Offices;</li>
      <li>(1) 10'8" X 12' Office;</li>
      <li>(1) Women's Restroom;</li>
      <li>(1) Men's Restroom;</li>
      <li>(1) Unisex Restroom;</li>
      <li>(1) 21'11" X 13' Conference Room;</li>
      <li>(1) Approximately 29' X 20' Training Room;</li>
      <li>(1) 26' X 11' Expanded Copy/Work Room;</li>
      <li>(1) 14' X 18'8" Break Room;</li>
      <li>(1) 16' X 12' Tech Supervision Room;</li>
      <li>(Multiple) Storage Closets;</li>
    </ul>
  </div>
  <div class="config" style="left:142px;top:284px">
    <h3>Warehouse Configuration :</h3>
    <ul>
      <li>(3) Grade-Level Loading Doors;</li>
      <li>Approximately 22' Eave Height;</li>
      <li>3-Phase Power;</li>
      <li>Room For Fenced Outside Storage;</li>
      <li>Plenty of Parking;</li>
      <li>Large Dumpster Enclosure;</li>
    </ul>
  </div>

  <div class="framed framed--thick" style="left:274px;top:220px;width:214px;height:139px"></div>
  <div class="photo photo--kitchen" style="left:280px;top:226px;width:202px;height:127px" role="img" aria-label="Photo of the break room with cabinets, table and chairs"></div>
  <div class="framed framed--thick" style="left:274px;top:369px;width:214px;height:141px"></div>
  <div class="photo photo--warehouse" style="left:280px;top:375px;width:202px;height:129px" role="img" aria-label="Photo of the open warehouse interior with concrete floor"></div>

  <div class="footer footer--details">
    <div class="contact" style="left:292px;top:15px">
      <svg width="16" height="16" viewBox="0 0 20 20"><circle cx="10" cy="10" r="8.5" fill="none" stroke="#fff" stroke-width="1.4"/><path d="M7 5.5l1.6 2.2-1 1.2c.6 1.3 1.6 2.3 2.9 2.9l1.2-1 2.2 1.6-.9 1.6c-3.6-.4-6.3-3.1-6.7-6.7z" fill="#fff"/></svg>
      <span>(555)014-2287</span>
    </div>
    <div class="contact" style="left:292px;top:43px">
      <svg width="16" height="12" viewBox="0 0 20 14"><rect x="1" y="1" width="18" height="12" fill="none" stroke="#fff" stroke-width="1.4"/><path d="M1 1l9 7 9-7" fill="none" stroke="#fff" stroke-width="1.4"/></svg>
      <span>Wade@TLMVX.net</span>
    </div>
  </div>

  <div class="framed framed--thick" style="left:9px;top:492px;width:250px;height:122px;background:var(--paper)"></div>
  <div class="map" style="position:absolute;left:15px;top:498px;width:238px;height:110px" role="img" aria-label="Area map showing the property location north of the city"></div>
</section>

</body>
</html>
```